Business card needed for home based pen making business.

I'm after a business card that's a bit more than an off the shelf card. I do like the idea of a card split horizontal with different colours used. A third colour is to be used for the business name and if need a forth for the other details.

I don't have a logo and will pay extra for one ($150 extra). I mainly make pens and seam rippers (stitch unpicks). The logo may be used for a website in future, as will the colours so please provide the colour codes and font type.

I'd like the business name in an easy to read script font at the top (with logo if you have one) and the other details to the bottom left hand side. I'll leave it up to you to match the script to the font used for the other details.

I'd like to keep a triangular balance to the card so something like a siloet of pot containing pens on the bottom right could be used to balance it out. There my ideas I want to see your.

Business name: Quillo & Co
Email address: quilloandco@mailvista.net
Contact: Dorian
Phone: 0418 352 976
No address is to be used on card.

Target Market(s)

Wide variety of people visiting craft markets. Age range 30+.

Industry/Entity Type

Business

Contact Information for Business Card

Quill & Co

Font styles to use
Script

Colors
f0ecf4
3277b5
3176b5

Requirements
Must have
• Contact: Dorian
• Phone: 0418 352 976
• Email address: quilloandco@mailvista.net
Nice to have
• An icon and/or graphics depicting pens and seam rippers..
Should not have
• I don't want icon/ graphic to be a crossed pen and seam ripper.

```html
<!DOCTYPE html>
<html lang="en">
<head>
<meta charset="utf-8">
<title>Quillo &amp; Co — Business Card</title>
<link rel="stylesheet" href="https://fonts.googleapis.com/css2?family=Arimo:wght@400&family=Tinos:wght@400&display=swap">
<style>
  :root {
    --backdrop: #e4e6ea;
    --card: #ebe8ef;
    --strip-blue: #3b75b1;
    --cell-navy: #2e3d89;
    --cell-indigo: #3a4d9f;
    --cell-periwinkle: #5569b1;
    --name-band: #cde1ee;
    --ink-blue: #3277b5;
    --photo-light: #f0ecf4;
    --photo-warm: #ecd5cc;
    --icon-line: #ffffff;
  }
  * { margin: 0; padding: 0; box-sizing: border-box; }
  html, body { width: 1200px; height: 800px; overflow: hidden; }
  body {
    background: var(--backdrop);
    font-family: "Arimo", Arial, sans-serif;
  }
  .canvas { position: relative; width: 1200px; height: 800px; }
  .card {
    position: absolute;
    left: 390px; top: 50px;
    width: 420px; height: 700px;
    background: var(--card);
    box-shadow: 0 6px 24px rgba(40, 60, 100, 0.18);
    overflow: hidden;
  }
  .accent-strip {
    position: absolute;
    left: 12px; top: 0;
    width: 81px; height: 403px;
    background: var(--strip-blue);
  }
  .hero-image {
    position: absolute;
    left: 93px; top: 0;
    width: 327px; height: 403px;
    background: linear-gradient(155deg, var(--photo-warm) 0%, #efe2de 35%, var(--photo-light) 70%);
  }
  .brand-name {
    position: absolute;
    left: 93px; top: 310px;
    width: 327px;
    text-align: center;
    font-family: "Arimo", Arial, sans-serif;
    font-size: 34px;
    font-weight: 400;
    color: var(--ink-blue);
  }
  .name-band {
    position: absolute;
    left: 93px; top: 403px;
    width: 327px; height: 68px;
    background: var(--name-band);
  }
  .icon-cell {
    position: absolute;
    left: 12px;
    width: 81px; height: 68px;
    display: flex; align-items: center; justify-content: center;
  }
  .icon-cell--person { top: 403px; background: var(--cell-navy); }
  .icon-cell--phone  { top: 471px; background: var(--cell-indigo); }
  .icon-cell--link   { top: 539px; background: var(--cell-periwinkle); }
  .icon-cell svg { width: 40px; height: 40px; }
  .detail {
    position: absolute;
    left: 114px;
    color: var(--ink-blue);
  }
  .detail--contact { top: 421px; font-size: 23px; }
  .detail--phone   { top: 495px; font-size: 17px; font-family: "Tinos", "Times New Roman", serif; }
  .detail--email   { top: 556px; font-size: 17px; }
</style>
</head>
<body>
<div class="canvas">
  <div class="card">
    <div class="accent-strip"></div>
    <div class="hero-image" role="img" aria-label="Soft photograph of a hand holding a handmade seam ripper"></div>
    <div class="brand-name">Quillo &amp; Co</div>

    <div class="name-band"></div>

    <div class="icon-cell icon-cell--person">
      <svg viewBox="0 0 40 40" fill="none" stroke="var(--icon-line)" stroke-width="1.6" aria-hidden="true">
        <circle cx="20" cy="20" r="17"/>
        <circle cx="20" cy="16" r="6"/>
        <path d="M9 32c2-6 6-9 11-9s9 3 11 9"/>
      </svg>
    </div>
    <div class="icon-cell icon-cell--phone">
      <svg viewBox="0 0 40 40" fill="none" stroke="var(--icon-line)" stroke-width="1.6" aria-hidden="true">
        <path d="M6 14c0-4 6-6 14-6s14 2 14 6l-1 3h-6l-1-3h-12l-1 3h-6z"/>
        <rect x="11" y="18" width="18" height="16" rx="2"/>
        <g fill="var(--icon-line)" stroke="none">
          <circle cx="16" cy="23" r="1.3"/><circle cx="20" cy="23" r="1.3"/><circle cx="24" cy="23" r="1.3"/>
          <circle cx="16" cy="27" r="1.3"/><circle cx="20" cy="27" r="1.3"/><circle cx="24" cy="27" r="1.3"/>
          <circle cx="16" cy="31" r="1.3"/><circle cx="20" cy="31" r="1.3"/><circle cx="24" cy="31" r="1.3"/>
        </g>
      </svg>
    </div>
    <div class="icon-cell icon-cell--link">
      <svg viewBox="0 0 40 40" fill="none" stroke="var(--icon-line)" stroke-width="1.6" aria-hidden="true">
        <rect x="17" y="6" width="10" height="18" rx="5" transform="rotate(45 22 15)"/>
        <rect x="13" y="16" width="10" height="18" rx="5" transform="rotate(45 18 25)"/>
      </svg>
    </div>

    <div class="detail detail--contact">Dorian</div>
    <div class="detail detail--phone">0418 352 976</div>
    <div class="detail detail--email">quilloandco@mailvista.net</div>
  </div>
</div>
</body>
</html>
```